Medicinal Cannabis Patient Monitoring App

We have a BASIC design for our app for monitoring patients who received Medicinal Cannabis.
The patient would rate how they're feeling after each dose.

The general flow once user is logged in and set up in the system is:

- User should be able to enter the dosing information for the current day
* Consumption Details:
> Enter Time
> Enter Dosage Taken (Added during onboarding)
> Method take to consume the drug
* Score Details:
> Pain Score (On the scale of 1-10)
> Nausea Score (On the scale of 1-10)
> Sedation Score (On the scale of 1-10)
> Wellbeing Score (On the scale of 1-10)
* Blood Pressure Details:
> Pulse
> Blood Pressure Readings
- User should be able to view the instructions
- User should be able to submit the entered details in the platform

We're looking for a clean, medical and SIMPLE design.

OUR USERS are often ELDERLY, Children and disabled individuals. You must consider this in the design.
So, for example, when designing sliders you should consider a creative way to explain the meaning of the slider if the person cant read the word description.

Designs look the same

```html
<!DOCTYPE html>
<html lang="en">
<head>
<meta charset="utf-8">
<title>Medicinal Cannabis – Patient Monitoring Screens</title>
<link rel="stylesheet" href="https://fonts.googleapis.com/css2?family=Lato:wght@400;700&family=Ubuntu:wght@500&display=swap">
<style>
  :root{
    --bg:#e4e4e4;
    --white:#ffffff;
    --green-top:#7cc93a;
    --green-bot:#3e9a22;
    --green-text:#3f8f1c;
    --orange-top:#ffae2b;
    --orange-bot:#f78a0f;
    --ink:#333333;
    --muted:#7a7a7a;
    --line:#dcdcdc;
    --pain:#3f9a1f;
    --nausea:#17a58a;
    --sedation:#e0871a;
    --wellbeing:#8fbf1e;
  }
  *{box-sizing:border-box;margin:0;padding:0}
  html,body{width:1200px;height:772px;overflow:hidden}
  body{background:var(--bg);position:relative;font-family:"Lato",sans-serif;color:var(--ink)}

  .screen{position:absolute;background:var(--white);overflow:hidden;border-radius:22px;box-shadow:0 4px 18px rgba(0,0,0,.12)}
  .screen--dose{left:100px;top:68px;width:286px;height:604px}
  .screen--feeling{left:472px;top:72px;width:284px;height:486px}
  .screen--readings{left:842px;top:72px;width:284px;height:448px}

  .app-bar{position:absolute;left:0;right:0;height:46px;background:linear-gradient(var(--green-top),var(--green-bot));display:flex;align-items:center;color:var(--white)}
  .app-bar__menu{width:24px;margin-left:14px;margin-right:32px}
  .app-bar__menu span{display:block;height:3px;background:var(--white);margin:4px 0;border-radius:1px}
  .app-bar__title{font-family:"Ubuntu",sans-serif;font-weight:500;font-size:18px;letter-spacing:.2px}

  .footer{position:absolute;left:0;right:0;text-align:center;font-size:8px;color:#555}

  /* Dose screen */
  .dose-title{position:absolute;top:84px;left:0;right:0;text-align:center;color:var(--green-text);font-weight:700;font-size:15px}
  .picker{position:absolute;top:118px;left:0;right:0}
  .picker__row{height:26px;border-top:1px solid var(--line);display:flex;align-items:center;font-size:11.5px;color:var(--muted)}
  .picker__row span:nth-child(1){width:100px;text-align:right}
  .picker__row span:nth-child(2){width:44px;text-align:right}
  .picker__row span:nth-child(3){width:30px;text-align:right}
  .picker__row--active{height:34px;background:linear-gradient(var(--orange-top),var(--orange-bot));color:var(--white);font-size:14px;font-weight:700}
  .picker__row--active span:nth-child(1){width:118px}
  .picker__row--active span:nth-child(2){width:38px}
  .picker__row--active span:nth-child(4){width:42px;text-align:right}
  .photo{position:absolute;left:0;right:0}
  .photo--dose{top:255px;height:304px;background:linear-gradient(120deg,#d8c2b0,#efe2d6 45%,#c9a996)}
  .dose-card{position:absolute;left:25px;top:280px;width:239px;height:250px;background:rgba(255,255,255,.93);text-align:center}
  .dose-card__title{margin-top:26px;font-size:17px;font-weight:700;color:#444}
  .dose-input{display:flex;justify-content:center;align-items:center;margin-top:12px;padding-left:22px}
  .dose-input__field{width:114px;height:30px;border:1px solid #bbb;background:var(--white)}
  .dose-input__unit{margin-left:6px;color:var(--green-top);font-size:16px}
  .methods{display:flex;justify-content:center;gap:20px;margin-top:24px}
  .method{width:50px;font-size:11.5px;color:#444}
  .method svg{display:block;margin:0 auto 7px}
  .btn{position:absolute;color:var(--white);font-weight:700;font-size:13px;display:flex;align-items:center;justify-content:center}
  .btn--next{left:25px;width:191px;top:205px;height:33px;background:linear-gradient(var(--green-top),var(--green-bot))}

  /* Feeling screen */
  .photo--feeling{top:76px;height:438px;background:linear-gradient(135deg,#ececec,#cfcfcf 60%,#b9b9b9)}
  .feeling-title{position:absolute;top:156px;left:0;right:0;text-align:center;font-size:18px;font-weight:700;color:#333}
  .scale{position:absolute;left:21px;width:243px;background:var(--white);box-shadow:0 1px 4px rgba(0,0,0,.15)}
  .scale svg{position:absolute;left:20px;top:12px}
  .scale__low,.scale__high{position:absolute;top:33px;font-size:9px;font-weight:700;color:#444}
  .scale__low{left:20px}.scale__high{right:20px}
  .scale__label{position:absolute;top:30px;left:0;right:0;text-align:center;font-size:14px;color:#555}

  /* Readings screen */
  .photo--readings{top:80px;height:316px;background:linear-gradient(160deg,#c8ecdd,#a8e3e6 50%,#d9efcf)}
  .readings-title{position:absolute;top:152px;left:0;right:0;text-align:center;font-size:18px;font-weight:700;color:#333}
  .readings-card{position:absolute;left:18px;top:144px;width:252px;height:146px;background:rgba(255,255,255,.85)}
  .field{position:absolute;left:20px;right:19px;display:flex;align-items:center;justify-content:space-between;font-size:11.5px;font-weight:700;color:#555}
  .field__input{width:101px;height:26px;border:1px solid #aaa;background:var(--white)}
  .btn--submit{left:20px;top:102px;width:213px;height:28px;background:linear-gradient(var(--orange-top),var(--orange-bot))}
  .readings-note{position:absolute;top:306px;left:0;right:0;text-align:center;font-size:12.5px;line-height:19px;color:#333}
</style>
</head>
<body>

<section class="screen screen--dose">
  <header class="app-bar" style="top:28px"><div class="app-bar__menu"><span></span><span></span><span></span></div><div class="app-bar__title">Medicinal Cannabis</div></header>
  <h2 class="dose-title">ENTER TIME OF TAKING DRUG</h2>
  <div class="picker">
    <div class="picker__row"><span>Sun 28 Jan</span><span>10</span><span>55</span></div>
    <div class="picker__row"><span>Mon 29 Jan</span><span>11</span><span>50</span></div>
    <div class="picker__row picker__row--active"><span>Today</span><span>12</span><span>00</span><span>pm</span></div>
    <div class="picker__row"><span>Wed 31 Jan</span><span>10</span><span>05</span></div>
    <div class="picker__row"><span>Thr 01 Feb</span><span>11</span><span>10</span></div>
  </div>
  <div class="photo photo--dose" role="img" aria-label="Soft photo of a patient taking medication"></div>
  <div class="dose-card">
    <h3 class="dose-card__title">ENTER DOSE TAKEN</h3>
    <div class="dose-input"><div class="dose-input__field"></div><span class="dose-input__unit">Gm</span></div>
    <div class="methods">
      <div class="method"><svg width="48" height="48" viewBox="0 0 48 48"><circle cx="24" cy="24" r="23" fill="#f7941d"/><circle cx="24" cy="24" r="13" fill="none" stroke="#fff" stroke-width="2"/><path d="M24 11v26M11 24h26" stroke="#fff" stroke-width="2"/></svg>TABLET</div>
      <div class="method"><svg width="48" height="48" viewBox="0 0 48 48"><circle cx="24" cy="24" r="23" fill="#fff" stroke="#3e9a22" stroke-width="1.5"/><path d="M15 22a5 5 0 0 1 8-4 6 6 0 0 1 11 3 4 4 0 0 1 0 8H16a4 4 0 0 1-1-7z" fill="none" stroke="#3e9a22" stroke-width="1.6"/><path d="M19 32c3 2 9 2 12 0M22 14c2-2 5-2 6 0" fill="none" stroke="#3e9a22" stroke-width="1.6"/></svg>SMOKE</div>
      <div class="method"><svg width="48" height="48" viewBox="0 0 48 48"><circle cx="24" cy="24" r="23" fill="#fff" stroke="#3e9a22" stroke-width="1.5"/><rect x="18" y="20" width="12" height="18" rx="2" fill="none" stroke="#3e9a22" stroke-width="1.6"/><rect x="21" y="12" width="6" height="8" fill="none" stroke="#3e9a22" stroke-width="1.6"/><path d="M21 26h6M21 30h6" stroke="#3e9a22" stroke-width="1.6"/></svg>VAPE</div>
    </div>
    <div class="btn btn--next">NEXT</div>
  </div>
  <p class="footer" style="top:573px">© 2018 Company Name&nbsp; All right reserved</p>
</section>

<section class="screen screen--feeling">
  <header class="app-bar" style="top:30px"><div class="app-bar__menu"><span></span><span></span><span></span></div><div class="app-bar__title">Medicinal Cannabis</div></header>
  <div class="photo photo--feeling" role="img" aria-label="Faded photo of a smiling patient"></div>
  <h2 class="feeling-title" style="top:84px">How are you feeling?</h2>
  <div class="scale" style="top:150px;height:58px"><svg width="203" height="14"><line x1="7" y1="7" x2="196" y2="7" stroke="var(--pain)" stroke-width="4"/><circle cx="7" cy="7" r="5" fill="#fff" stroke="var(--pain)" stroke-width="2.5"/><circle cx="196" cy="7" r="5" fill="#fff" stroke="var(--pain)" stroke-width="2.5"/></svg><span class="scale__low">01</span><span class="scale__label">Pain</span><span class="scale__high">10</span></div>
  <div class="scale" style="top:212px;height:62px"><svg width="203" height="14"><line x1="7" y1="7" x2="196" y2="7" stroke="var(--nausea)" stroke-width="4"/><circle cx="7" cy="7" r="5" fill="#fff" stroke="var(--nausea)" stroke-width="2.5"/><circle cx="196" cy="7" r="5" fill="#fff" stroke="var(--nausea)" stroke-width="2.5"/></svg><span class="scale__low">01</span><span class="scale__label">Nausea</span><span class="scale__high">10</span></div>
  <div class="scale" style="top:278px;height:60px"><svg width="203" height="14"><line x1="7" y1="7" x2="196" y2="7" stroke="var(--sedation)" stroke-width="4"/><circle cx="7" cy="7" r="5" fill="#fff" stroke="var(--sedation)" stroke-width="2.5"/><circle cx="196" cy="7" r="5" fill="#fff" stroke="var(--sedation)" stroke-width="2.5"/></svg><span class="scale__low">01</span><span class="scale__label">Sedation</span><span class="scale__high">10</span></div>
  <div class="scale" style="top:342px;height:61px"><svg width="203" height="14"><line x1="7" y1="7" x2="196" y2="7" stroke="var(--wellbeing)" stroke-width="4"/><circle cx="7" cy="7" r="5" fill="#fff" stroke="var(--wellbeing)" stroke-width="2.5"/><circle cx="196" cy="7" r="5" fill="#fff" stroke="var(--wellbeing)" stroke-width="2.5"/></svg><span class="scale__low">01</span><span class="scale__label">Wellbeing</span><span class="scale__high">10</span></div>
  <p class="footer" style="top:456px">© 2018 Company Name&nbsp; All right reserved</p>
</section>

<section class="screen screen--readings">
  <header class="app-bar" style="top:32px"><div class="app-bar__menu"><span></span><span></span><span></span></div><div class="app-bar__title">Medicinal Cannabis</div></header>
  <div class="photo photo--readings" role="img" aria-label="Soft aqua medical background with heart-rate trace"></div>
  <h2 class="readings-title" style="top:106px">READINGS</h2>
  <div class="readings-card">
    <div class="field" style="top:20px"><span>PULSE</span><div class="field__input"></div></div>
    <div class="field" style="top:58px"><span>BLOOD PRESSURE</span><div class="field__input"></div></div>
    <div class="btn btn--submit">SUBMIT</div>
  </div>
  <p class="readings-note">These are now being Uploaded<br>to the Confidential Data Base</p>
  <p class="footer" style="top:409px">© 2018 Company Name&nbsp; All right reserved</p>
</section>

</body>
</html>
```